Etiketten für Wein und Sekt
Zielgruppe
Sekt- und Weinherstellung
Zielgruppe 25 - 60 Jahre
Aufgabenstellung
Wir führen ein neues Produkt in den Markt ein:
gewünschter Name: The Velvet Dusk Mood
Hervorgehoben werden soll 'Velvet Dusk'
auf dieser Basis suchern wir einmal das Etikett für den WEIN
und einmal das Etikett für den SEKT (gleiches Design/Designfamilie)
Beim Sekt dachten wir an den Zusatz Sparkling auf dem Etikett?
Achtung, es handelt sich hier um keinen Eiswein !
Damit darf unser Produkt nicht in Verbindung gebracht werden (dt. Weinrecht)
Unser Wein/Sekt ist ein fruchtiger Rose Wein/Sekt
Ein Cuvée aus regionalen Rebsorten
Beim Trinkgenuss sollen die Gedanken an gefrorene Beeren/Trauben gehen.
Wir dachten an Beerentöne und Rosegold (wie der Inhalt)
Aktuell verwenden wir Etikettenformen in Rechteckgröße horizontal oder vertikal
Besten Dank im Voraus !!

```html
<!DOCTYPE html>
<html lang="en">
<head>
<meta charset="utf-8">
<title>The Velvet Dusk Mood – Wine &amp; Sparkling Labels</title>
<link rel="stylesheet" href="https://fonts.googleapis.com/css2?family=Alfa+Slab+One&display=swap">
<style>
  :root {
    --frame-light: #f8cdbf;
    --frame-mid: #f4a992;
    --frame-deep: #ef927a;
    --ice-light: #d5ecec;
    --ice-mid: #b2dcdd;
    --ice-deep: #86cbcf;
    --berry-ink: #b3645a;
    --sparkle-white: #ffffff;
    --emblem-light: #e3ecf1;
    --emblem-shade: #bfd3da;
  }
  * { margin: 0; padding: 0; box-sizing: border-box; }
  html, body {
    width: 1200px;
    height: 561px;
    overflow: hidden;
    background: #ffffff;
  }
  .canvas {
    position: relative;
    width: 1200px;
    height: 561px;
  }
  .label {
    position: absolute;
    top: 0;
    width: 561px;
    height: 561px;
    background: linear-gradient(135deg, var(--frame-light) 0%, var(--frame-mid) 45%, var(--frame-deep) 70%, var(--frame-light) 100%);
  }
  .label--wine { left: 0; }
  .label--sparkling { left: 639px; }
  .label__field {
    position: absolute;
    left: 20px;
    top: 18px;
    width: 525px;
    height: 523px;
    background: linear-gradient(150deg, var(--ice-light) 0%, var(--ice-mid) 35%, var(--ice-deep) 55%, var(--ice-mid) 75%, var(--ice-light) 100%);
  }
  .label__emblem {
    position: absolute;
    left: 194px;
    top: 28px;
    width: 142px;
    height: 225px;
    border-radius: 50% 50% 46% 46% / 40% 40% 60% 60%;
    background: radial-gradient(circle at 45% 40%, var(--emblem-light) 0%, var(--emblem-shade) 100%);
    opacity: 0.85;
  }
  .label__title {
    position: absolute;
    left: 0;
    width: 525px;
    text-align: center;
    font-family: "Alfa Slab One", serif;
    color: var(--berry-ink);
    line-height: 1;
    mix-blend-mode: multiply;
  }
  .title__the { top: 280px; font-size: 38px; }
  .title__line1 { top: 322px; font-size: 80px; }
  .title__line2 { top: 393px; font-size: 80px; }
  .label__variant {
    position: absolute;
    left: 0;
    width: 525px;
    top: 469px;
    text-align: center;
    font-family: "Alfa Slab One", serif;
    font-size: 35px;
    line-height: 1;
  }
  .variant--wine { color: var(--berry-ink); mix-blend-mode: multiply; }
  .variant--sparkling { color: var(--sparkle-white); }
</style>
</head>
<body>
<main class="canvas">
  <section class="label label--wine">
    <div class="label__field">
      <div class="label__emblem" role="img" aria-label="Paper-cut grape cluster emblem with leaf and curled tendril"></div>
      <h1>
        <span class="label__title title__the">THE</span>
        <span class="label__title title__line1">VELVET</span>
        <span class="label__title title__line2">DUSK</span>
      </h1>
      <p class="label__variant variant--wine">MOOD</p>
    </div>
  </section>

  <section class="label label--sparkling">
    <div class="label__field">
      <div class="label__emblem" role="img" aria-label="Paper-cut grape cluster emblem with leaf and curled tendril"></div>
      <h2>
        <span class="label__title title__the">THE</span>
        <span class="label__title title__line1">VELVET</span>
        <span class="label__title title__line2">DUSK</span>
      </h2>
      <p class="label__variant variant--sparkling">SPARKLING</p>
    </div>
  </section>
</main>
</body>
</html>
```